Home page web design for "Tales from Thee"

We need a home page web design for a start up company that will write memoirs for seniors.
The completed project will need to include PSD files...NO HTML or CSS necessary.
Attached is a brief outline concept that may give you some ideas...but you are the creative professionals, so please feel free to add your ideas. We will also attach some files that show you our logo, brochures, and photos that could be used to give you ideas of our focus.
There will need to be access to the other pages on the home page to include: 'About Us'; 'How We Can Help'; 'Community Sessions'; 'Senior Consulting ' and 'Contact Us'.
Updates

Target Market(s)

Seniors and Baby Boomers

Industry/Entity Type

It Company

Number of Pages Required

1 page

Colors
f9ba93
fbca95
faa54b
faf289
f37123

Requirements
Must have
• Script easy on senior eyes.
• Initial contact number would be 844-4LANTERN
Nice to have
• While the color pallet is non-specific we prefer the warm colors.
• salmon, peach.......
• NOT so much the orange of Halloween:)
• However, please utilize your creativity and put in colors you feel will draw best with your design.

```html
<!DOCTYPE html>
<html lang="en">
<head>
<meta charset="utf-8">
<title>Tales from Thee — Home</title>
<link href="https://fonts.googleapis.com/css2?family=Marcellus&family=Marcellus+SC&family=Open+Sans:wght@400;600&display=swap" rel="stylesheet">
<style>
:root{
  --orange:#f37123;
  --orange-soft:#f9a04b;
  --peach:#f9ba93;
  --gold:#c9963a;
  --header-bg:#eeedec;
  --light-bg:#f8f7f6;
  --mid-bg:#f1f0ef;
  --services-bg:#e8e4e1;
  --footer-bg:#c9c8c7;
  --text:#6b6b6b;
  --white:#ffffff;
}
*{margin:0;padding:0;box-sizing:border-box}
html,body{width:1200px;height:960px;overflow:hidden;background:var(--white)}
body{font-family:"Open Sans",Arial,sans-serif;color:var(--text);position:relative}
.page{position:absolute;left:426px;top:0;width:347px;height:960px;overflow:hidden}
.abs{position:absolute}

/* header */
.site-header{position:absolute;left:0;top:0;width:347px;height:43px;background:var(--header-bg)}
.brand{position:absolute;left:39px;top:2px;width:67px;height:38px;border:1px solid #c9b79a;display:flex;align-items:center;justify-content:center;font-family:"Marcellus",Georgia,serif;font-size:7.5px;color:#9a8465}
.contact-top{position:absolute;right:37px;top:5px;text-align:right;font-family:"Marcellus",Georgia,serif;color:var(--gold);line-height:10px}
.contact-top .phone{font-size:11px;letter-spacing:.5px;font-weight:bold;line-height:13px}
.contact-top .name{font-size:8.5px;letter-spacing:.4px}
.contact-top .name .sq{display:inline-block;width:8px;height:6px;background:var(--gold);margin-right:3px;vertical-align:0}

/* nav */
.main-nav{position:absolute;left:0;top:43px;width:347px;height:21px;background:var(--orange-soft);display:flex;align-items:center;padding-left:36px}
.main-nav a{color:var(--white);text-decoration:none;font-size:5.5px;letter-spacing:.2px;padding:0 3px;height:21px;line-height:21px;margin-right:3px}
.main-nav a.active{background:var(--orange)}
.main-nav .home{width:14px;display:flex;align-items:center;justify-content:center;padding:0}

/* hero */
.hero{position:absolute;left:0;top:64px;width:347px;height:151px}
.hero-photo{position:absolute;inset:0;background:linear-gradient(100deg,#b5642d 0%,#d38447 35%,#c98a5f 60%,#8a5a3c 85%,#6a4631 100%)}
.hero-caption{position:absolute;left:0;top:85px;width:174px;height:66px;background:rgba(231,112,40,.92);font-family:"Marcellus SC",Georgia,serif;color:var(--white);font-size:17px;line-height:21px;padding:10px 0 0 7px}
.hero-dots{position:absolute;right:15px;bottom:4px;display:flex;gap:2px}
.hero-dots span{width:4px;height:4px;border-radius:50%;background:#f1ece6}
.hero-dots span.on{background:var(--orange-soft)}

/* section headings */
.section-title{position:absolute;left:0;width:347px;text-align:center;font-family:"Marcellus",Georgia,serif;color:var(--orange);font-size:16.5px;letter-spacing:.3px}

/* who we are */
.who{position:absolute;left:0;top:215px;width:347px;height:167px;background:var(--light-bg)}
.who .rule{position:absolute;left:82px;top:41px;width:184px;height:1px;background:#e9a27a}
.who .copy{position:absolute;left:62px;top:58px;width:224px;text-align:center;font-size:5.2px;line-height:6.5px}
.who .copy p{margin-bottom:6.5px}

/* help */
.help{position:absolute;left:0;top:382px;width:347px;height:193px;background:var(--mid-bg)}
.help .sub{position:absolute;left:0;top:34px;width:347px;text-align:center;font-size:6px}
.help-item{position:absolute;top:60px;width:80px;text-align:center}
.help-item .ring{width:50px;height:50px;margin:0 auto;border-radius:50%;border:1px solid #cfcfcf;display:flex;align-items:center;justify-content:center;background:var(--light-bg)}
.help-item .ring.filled{background:var(--peach);border-color:var(--peach)}
.help-item h3{font-family:"Marcellus",Georgia,serif;color:var(--orange-soft);font-size:8px;margin-top:9px}
.help-item p{font-size:5.2px;line-height:6.5px;margin-top:7px}
.more-btn{display:inline-block;margin-top:6px;width:21px;height:6px;background:var(--orange);color:var(--white);font-size:4px;line-height:6px}

/* services */
.services{position:absolute;left:0;top:575px;width:347px;height:192px;background:var(--services-bg)}
.service-card{position:absolute;top:48px;width:88px;height:125px;background:var(--white)}
.service-card h3{height:25px;background:var(--orange);color:var(--white);font-family:"Marcellus",Georgia,serif;font-size:6px;font-weight:normal;padding:9px 0 0 3px}
.service-card .photo{height:58px}
.service-card p{font-size:5px;line-height:7px;padding:4px 4px 0}
.service-card .bar{margin:3px 4px 0;width:14px;height:2px;background:var(--orange)}

/* newsletter */
.newsletter{position:absolute;left:0;top:767px;width:347px;height:113px;background:var(--orange-soft)}
.newsletter h2{position:absolute;left:88px;top:13px;font-family:"Marcellus",Georgia,serif;font-weight:normal;color:var(--white);font-size:16.5px;letter-spacing:.3px}
.newsletter .envelope{position:absolute;left:62px;top:17px}
.newsletter .sub{position:absolute;left:0;top:32px;width:347px;text-align:center;color:#fde6cc;font-size:5.5px;padding-left:28px}
.signup-field{position:absolute;left:62px;top:51px;width:157px;height:15px;border:1px solid #fde1c2;color:#fde6cc;font-size:4.5px;line-height:13px;padding-left:9px}
.signup-btn{position:absolute;left:222px;top:51px;width:52px;height:15px;background:var(--white);color:var(--orange-soft);font-size:7px;line-height:15px;text-align:center}
.social{position:absolute;left:121px;top:81px;display:flex;gap:6px}
.social span{width:21px;height:21px;border:1px solid var(--white);border-radius:50%}

/* footer */
.site-footer{position:absolute;left:0;top:880px;width:347px;height:80px;background:var(--footer-bg)}
.foot-col{position:absolute;top:16px;height:50px}
.foot-col h4{font-family:"Marcellus",Georgia,serif;font-weight:normal;color:var(--gold);font-size:8.5px;letter-spacing:.3px}
.foot-col p{font-size:5.5px;line-height:10px;margin-top:6px;color:#6f6f6f}
.foot-col.small p{font-size:4.3px;line-height:8px;margin-top:8px}
.foot-divider{position:absolute;top:10px;width:1px;height:55px;background:#adadad}
.foot-follow{display:flex;gap:7px;margin-top:8px}
.foot-follow span{width:5px;height:5px;background:#8a8a8a}
.foot-follow span.accent{background:var(--gold)}
.copyright{position:absolute;left:38px;top:69px;font-size:3.6px;color:#7a7a7a}
.copyright u{color:var(--orange)}
</style>
</head>
<body>
<div class="page">

  <header class="site-header">
    <div class="brand">Tales from Thee</div>
    <div class="contact-top">
      <div class="phone">+844-4LANTERN</div>
      <div class="name">Helen Marsh</div>
      <div class="name"><span class="sq"></span>J.R. Olwen</div>
    </div>
  </header>

  <nav class="main-nav">
    <a class="home" href="#" aria-label="Home">
      <svg width="7" height="7" viewBox="0 0 10 10"><path d="M5 0 L10 5 H8.5 V10 H6 V7 H4 V10 H1.5 V5 H0 Z" fill="#fff"/></svg>
    </a>
    <a class="active" href="#">About Us</a>
    <a href="#">How We Can Help</a>
    <a href="#">Community Services</a>
    <a href="#">Consulting Services</a>
    <a href="#">Contact Us</a>
  </nav>

  <section class="hero">
    <div class="hero-photo" role="img" aria-label="Photo of a smiling senior couple reading a book together"></div>
    <div class="hero-caption">When a genealogy<br>doesn’t say enough!</div>
    <div class="hero-dots"><span></span><span></span><span class="on"></span></div>
  </section>

  <section class="who">
    <h2 class="section-title" style="top:12px">WHO WE ARE</h2>
    <div class="rule"></div>
    <div class="copy">
      <p>We are not all presidents of countries or CEO's of fortune 500 companies! But "every life legacy is a gift to be treasured by the next generation."</p>
      <p>Does your family host generations of soldiers, doctors, farmers, scientists, mechanics, entrepreneurs, writers, politicians, contractors, pastors, artisans, athletes, musicians, etc.? Generational patterns can often emerge when writing your story that will interest the next generation.</p>
      <p>A genealogy, while very relevant, doesn't offer the personal story of the names we find. A biography can place a deeper relevance on the face for future descendants. Every life is a legacy to pass forward and we at Tales from Thee believe everyone should chronicle their life journey in writing. This commitment allows you to be remembered for who you truly are as a person.</p>
    </div>
  </section>

  <section class="help">
    <h2 class="section-title" style="top:13px">HOW WE CAN HELP YOU</h2>
    <div class="sub">we offer warm welcome &amp; safe pair of help for senior memoirs</div>

    <div class="help-item" style="left:40px">
      <div class="ring">
        <svg width="30" height="30" viewBox="0 0 30 30" fill="#9a9a9a"><path d="M15 17 C9 12 8 8 11 6.5 C13 5.5 14.5 7 15 8 C15.5 7 17 5.5 19 6.5 C22 8 21 12 15 17Z"/><path d="M3 14 C5 18 9 22 14 24 L14 27 L9 27 C5 24 2 19 3 14Z"/><path d="M27 14 C25 18 21 22 16 24 L16 27 L21 27 C25 24 28 19 27 14Z"/></svg>
      </div>
      <h3>Care &amp; Support</h3>
      <p>Lorem ipsum dolor sit amet, consectetur adipisicing elit, sed do eiusmod tempor incididunt ut labore et dolore magna aliqua.</p>
      <span class="more-btn">More</span>
    </div>

    <div class="help-item" style="left:133px">
      <div class="ring filled">
        <svg width="30" height="30" viewBox="0 0 30 30" fill="#fff"><circle cx="9" cy="8" r="2.5"/><circle cx="15" cy="7" r="2.8"/><circle cx="21" cy="8" r="2.5"/><rect x="6.5" y="11" width="5" height="9" rx="2"/><rect x="12.3" y="10.5" width="5.4" height="10" rx="2"/><rect x="18.5" y="11" width="5" height="9" rx="2"/><path d="M3 20 Q15 28 27 20 L27 22 Q15 30 3 22Z"/></svg>
      </div>
      <h3>Community Services</h3>
      <p>Lorem ipsum dolor sit amet, consectetur adipisicing elit, sed do eiusmod tempor incididunt ut labore et dolore magna aliqua.</p>
      <span class="more-btn">More</span>
    </div>

    <div class="help-item" style="left:226px">
      <div class="ring">
        <svg width="30" height="30" viewBox="0 0 30 30" fill="#9a9a9a"><path d="M11 8 V6 H19 V8 H17.5 V7.5 H12.5 V8Z"/><rect x="5" y="9" width="20" height="15" rx="1.5"/><rect x="13" y="14" width="4" height="3" fill="#f8f7f6"/></svg>
      </div>
      <h3>Hospice Services</h3>
      <p>Lorem ipsum dolor sit amet, consectetur adipisicing elit, sed do eiusmod tempor incididunt ut labore et dolore magna aliqua.</p>
      <span class="more-btn">More</span>
    </div>
  </section>

  <section class="services">
    <h2 class="section-title" style="top:15px">SERVICES WE PROVIDE</h2>

    <article class="service-card" style="left:36px">
      <h3>ARRIVAL OF GRANDCHILD</h3>
      <div class="photo" role="img" aria-label="Photo of a grandmother holding a new grandchild" style="background:linear-gradient(135deg,#d9d3c9,#a99782 60%,#7d6a58)"></div>
      <p>Lorem ipsum dolor sit amet, consectetur adipisicing elit, sed do eiusmod tempor incididunt</p>
      <div class="bar"></div>
    </article>

    <article class="service-card" style="left:130px">
      <h3>ANNIVERSERY</h3>
      <div class="photo" role="img" aria-label="Photo of a senior couple looking at an anniversary photo" style="background:linear-gradient(135deg,#8a6d56,#c79a6f 50%,#e3a46a)"></div>
      <p>Lorem ipsum dolor sit amet, consectetur adipisicing elit, sed do eiusmod tempor incididunt</p>
      <div class="bar"></div>
    </article>

    <article class="service-card" style="left:223px">
      <h3>BIRTHDAY</h3>
      <div class="photo" role="img" aria-label="Photo of a family celebrating a senior's birthday with cake" style="background:linear-gradient(135deg,#6e4a3e,#b37869 50%,#8e5b57)"></div>
      <p>Lorem ipsum dolor sit amet, consectetur adipisicing elit, sed do eiusmod tempor incididunt</p>
      <div class="bar"></div>
    </article>
  </section>

  <section class="newsletter">
    <svg class="envelope" width="17" height="11" viewBox="0 0 17 11"><rect x="0" y="0" width="17" height="11" fill="#fff"/><path d="M0 0 L8.5 6 L17 0" fill="none" stroke="#f9a04b" stroke-width="1"/><path d="M0 11 L6 5 M17 11 L11 5" stroke="#f9a04b" stroke-width=".8"/></svg>
    <h2>JOIN OUR NEWSLETTER</h2>
    <div class="sub">And always stay informed of the latest news &amp; events</div>
    <div class="signup-field">your email here</div>
    <div class="signup-btn">subscribed</div>
    <div class="social" aria-label="Social links"><span></span><span></span><span></span><span></span></div>
  </section>

  <footer class="site-footer">
    <div class="foot-col" style="left:37px">
      <h4>TELEPHONE</h4>
      <p>+844-4LANTERN<br>+717-555-0142</p>
    </div>
    <div class="foot-divider" style="left:104px"></div>
    <div class="foot-col" style="left:109px">
      <h4>ADRESS</h4>
      <p>Helen Marsh<br>J.R. Olwen</p>
    </div>
    <div class="foot-divider" style="left:173px"></div>
    <div class="foot-col small" style="left:178px">
      <h4>EMAIL US</h4>
      <p>info@talesfromthee.com<br>www.talesfromthee.com</p>
    </div>
    <div class="foot-divider" style="left:243px"></div>
    <div class="foot-col" style="left:248px">
      <h4>FOLLOW US</h4>
      <div class="foot-follow"><span></span><span class="accent"></span><span></span><span></span></div>
    </div>
    <div class="copyright">Copyright © 2013 Tales from Thee. All rights reserved. <u>Privacy policy</u></div>
  </footer>

</div>
</body>
</html>
```